Brindle Logistics Business Card Design

We are a trucking and warehousing company. We run freight in the US manly from the Pacific NW to TX and back up the the PNW. We also do warehousing where we store, move, and distribute freight. Looking for a clean and modern design of business card. We would like to look rich and elegant. Attached is our logo.

Industry/Entity Type

Trucking Company

Contact Information for Business Card

Looking for a clean and modern design of business card. We would like to look rich and elegant.

Font styles to use
Sans Serif

Colors

Designer to choose colors to be used in the design.

Requirements
Must have
• logo but it should not dominate the card
Should not have
• logo should not dominate the card

```html
<!DOCTYPE html>
<html lang="en">
<head>
<meta charset="utf-8">
<title>Brindle Logistics – Business Card</title>
<link href="https://fonts.googleapis.com/css2?family=Questrial&family=Mulish:ital,wght@0,700;1,700&display=swap" rel="stylesheet">
<style>
  :root {
    --backdrop: #4a3526;
    --card-dark: #333333;
    --mark-dark: #262626;
    --card-frame: #f7f7f7;
    --card-light: #e6e6e6;
    --ink: #333333;
  }
  * { margin: 0; padding: 0; box-sizing: border-box; }
  html, body { width: 1200px; height: 1200px; overflow: hidden; }
  body {
    position: relative;
    background: var(--backdrop);
    font-family: "Questrial", sans-serif;
    color: var(--ink);
  }
  .card { position: absolute; }
  .card-front {
    left: 218px; top: 132px; width: 753px; height: 428px;
    background: var(--card-dark);
  }
  .front-brand {
    position: absolute; left: 0; right: 0; top: 178px;
    text-align: center; color: var(--mark-dark);
    font-family: "Questrial", sans-serif; line-height: 1;
  }
  .front-brand .brand-name { font-size: 40px; letter-spacing: 1px; }
  .front-brand .brand-sub { font-size: 17px; letter-spacing: 1px; margin-top: 4px; }

  .card-back {
    left: 217px; top: 630px; width: 766px; height: 437px;
    background: var(--card-frame);
  }
  .back-panel {
    position: absolute; inset: 14px;
    background: var(--card-light);
  }
  .holder-name {
    position: absolute; left: 56px; top: 108px;
    font-size: 46px; line-height: 1; white-space: nowrap;
  }
  .holder-name .first { font-family: "Mulish", sans-serif; font-weight: 700; }
  .job-title {
    position: absolute; left: 63px; top: 155px;
    font-family: "Mulish", sans-serif; font-weight: 700; font-size: 21px;
  }
  .divider {
    position: absolute; left: 100px; top: 212px;
    width: 87px; height: 2px; background: var(--ink);
  }
  .contact {
    position: absolute; left: 63px; top: 231px;
    font-size: 18px; line-height: 21px;
  }
  .contact-row { display: flex; margin-bottom: 4px; }
  .contact-row dt {
    width: 85px; font-family: "Mulish", sans-serif;
    font-weight: 700; font-style: italic;
  }
  .back-brand {
    position: absolute; right: 51px; top: 123px;
    text-align: center; line-height: 1; color: var(--ink);
  }
  .back-brand .brand-name { font-size: 24px; letter-spacing: 0.5px; }
  .back-brand .brand-sub { font-size: 10.5px; letter-spacing: 0.5px; margin-top: 2px; }
</style>
</head>
<body>
  <section class="card card-front">
    <div class="front-brand">
      <div class="brand-name">BRINDLE</div>
      <div class="brand-sub">LOGISTICS, LLC</div>
    </div>
  </section>

  <section class="card card-back">
    <div class="back-panel">
      <h1 class="holder-name"><span class="first">YOUR</span> NAME</h1>
      <div class="job-title">job title</div>
      <div class="divider"></div>
      <dl class="contact">
        <div class="contact-row"><dt>address.</dt><dd>123 Lorem Ipsum,<br>Lorem, City 12345</dd></div>
        <div class="contact-row"><dt>email.</dt><dd>youremail@yourdomain.com</dd></div>
        <div class="contact-row"><dt>phone.</dt><dd>123.456.7891</dd></div>
      </dl>
      <div class="back-brand">
        <div class="brand-name">BRINDLE</div>
        <div class="brand-sub">LOGISTICS, LLC</div>
      </div>
    </div>
  </section>
</body>
</html>
```